Brightmorrow - a website to encourage people to spend time in nature

I have a squarespace site with some content on it but the squarespace template doesn't completely suit my needs, I keep fiddling with the template but actually I need some professional help to get it looking the way I want and with the right 'mood'.
The website is for "Brightmorrow" - it will be a blog where I write about the importance of nature for good health. I also want to use the website to market services such as outdoor coaching, retreats and walking workshops.
This has been in my head for a LONG time and I currently only use instagram for micro-blogs but it's time for me to get this moving. I've previously engaged other designers on branding for it but they just didn't get it quite the way that I wanted it and I wasn't completely happy with the results. It's been a process for me as to what I want but in the meantime I just didn't come back to the design aspect of it now. I'm looking for a designer who understands the purpose of the website, the ethos and can help me realise this into a design that's clean, clear and simple.

Please note that I have a domain (brightmorrow.example) and a lot of content drafted on squarespace already. I have published it with password protection - password is brightmorrow2020 - it still has some of the original template on it, but does have some content. Don't take it as anything to follow in particular, i am looking for fresh eyes and fresh ideas.
Updates

Need extra days to review

Target Market(s)

There are three main groups that I want to target - people who are suffering from stress and anxiety, people who treat them and parents who want to get their kids outside (thereby preventing stress and anxiety)

Contact Information for Business Card

Clara Dunmore
Brightmorrow
Telephone +44 7946 203857
brightmorrow@mailbox.example

Logo Text

Brightmorrow - if that. I have an idea that the logo should have a leaf on it somewhere, or maybe just be a leaf.

Coding

Coded - Design and coding required

Number of Pages Required

5+ page

Font styles to use
Serif
Sans Serif

Colors
add136
33b8a4
34a6d7
3377b5

Requirements
Must have
• Space for lots of images. The ability for me to edit the pages if I need to. Be user friendly. Look beautiful.
• For an idea of the images I use and the content I'm interested in writing about have a look at @brightmorrow on instagram.
• That pop up about cookies so I am complying with data laws.
Should not have
• Must not be too 'busy' I'd like to avoid too much movement.

```html
<!DOCTYPE html>
<html lang="en">
<head>
<meta charset="utf-8">
<title>Brightmorrow</title>
<link rel="stylesheet" href="https://fonts.googleapis.com/css2?family=Montserrat:wght@400;500;600;700;800&display=swap">
<style>
:root{
  --ink:#1c1d1f;
  --dark:#1f2022;
  --muted:#9a9a9a;
  --text:#4a4a4a;
  --leaf:#add136;
  --teal:#33b8a4;
  --sky:#34a6d7;
  --deep:#3377b5;
  --accent:#33b8a4;
  --line:#e4e4e4;
  --soft:#f0f6f3;
  --white:#ffffff;
}
*{box-sizing:border-box;margin:0;padding:0}
html,body{width:1200px;height:3149px;overflow:hidden;background:var(--white)}
body{position:relative;font-family:'Montserrat',sans-serif;color:var(--ink)}

/* header */
.site-header{position:absolute;left:0;top:0;width:1200px;height:122px;border:1px solid var(--line)}
.btn-subscribe{position:absolute;left:34px;top:61px;width:108px;height:33px;background:var(--deep);color:var(--white);font-size:9px;font-weight:700;letter-spacing:.5px;display:flex;align-items:center;justify-content:center}
.brand{position:absolute;left:0;width:1200px;top:38px;display:flex;justify-content:center;align-items:center;gap:12px}
.brand-mark{width:14px;height:14px;border-radius:50%;background:var(--leaf)}
.brand-name{font-size:40px;font-weight:400;letter-spacing:1px;color:var(--ink)}
.header-icons{position:absolute;top:62px;left:1024px;display:flex;gap:26px;align-items:center}
.dot-icon{width:13px;height:13px;border:1.5px solid var(--ink);border-radius:50%}

/* hero */
.hero-img{position:absolute;top:125px;height:464px}
.hero-left{left:4px;width:204px;background:linear-gradient(170deg,#d9c27a,#8a9a3e 40%,#4a5a2a)}
.hero-main{left:228px;width:740px;background:linear-gradient(100deg,#2f3d2c,#5f7250 35%,#c9d3c8 55%,#eef1ee 70%,#34432f)}
.hero-right{left:995px;width:205px;background:linear-gradient(180deg,#2a4a45,#1c3a36 50%,#2f4a2a)}
.hero-dots{position:absolute;top:556px;left:518px;display:flex;gap:18px}
.hero-dots span{display:block;height:2px;width:44px;background:rgba(255,255,255,.9)}
.hero-dots span+span{width:98px;background:rgba(255,255,255,.35)}

/* sidebar */
.widget-title{position:absolute;left:210px;width:174px;height:30px;display:flex;align-items:center;justify-content:center}
.widget-title::before,.widget-title::after{content:"";position:absolute;top:14px;width:8px;height:1px;background:var(--ink)}
.widget-title::before{left:0}.widget-title::after{right:0}
.widget-title span{border:1px solid var(--line);padding:0 14px;height:30px;line-height:30px;font-size:8.5px;font-weight:700;letter-spacing:.8px}
.avatar{position:absolute;left:257px;top:710px;width:80px;height:80px;border-radius:50%;background:linear-gradient(180deg,#9fb45a,#6f8a86 50%,#2c3a34)}
.about-text{position:absolute;left:204px;width:186px;top:810px;text-align:center;font-size:9px;line-height:17px;color:var(--text)}
.about-social{position:absolute;top:858px;left:244px;display:flex;gap:7px}
.about-social span{width:22px;height:22px;border-radius:50%;background:var(--ink);display:flex;align-items:center;justify-content:center}
.about-social span::after{content:"";width:6px;height:6px;border-radius:50%;background:var(--white)}
.join{position:absolute;left:210px;top:919px;width:174px;height:153px;border:1px solid var(--ink)}
.join-top{height:99px;background:linear-gradient(180deg,#3d4a3a,#26302a);display:flex;align-items:center;justify-content:center;color:var(--white);font-size:16px;font-weight:700}
.join-field{position:absolute;left:18px;right:18px;top:120px;height:18px;border-bottom:1px solid var(--line);font-size:8px;color:var(--muted)}
.join-field svg{position:absolute;right:0;top:0}
.recent{position:absolute;left:210px;display:flex;gap:12px}
.recent .thumb{width:64px;height:51px}
.recent h4{font-size:10.5px;font-weight:600;margin-top:8px}
.recent p{font-size:8px;color:var(--muted);letter-spacing:.5px;margin-top:3px}
.ads{position:absolute;left:210px;top:1381px;width:174px;height:172px;background:#f1f1f1;padding:12px}
.ads-inner{width:100%;height:100%;background:var(--white);position:relative}
.ads-inner b{position:absolute;right:16px;bottom:27px;font-size:13px;font-weight:600}
.ads-inner small{position:absolute;right:16px;bottom:13px;font-size:7px;color:var(--muted)}
.insta{position:absolute;left:210px;top:1642px;width:174px;display:grid;grid-template-columns:83px 83px;gap:7px 8px}
.insta div{height:83px}
.insta-handle{position:absolute;left:210px;width:174px;top:1826px;text-align:center;font-size:8px;font-weight:600;color:var(--teal);letter-spacing:.8px}
.cats{position:absolute;left:210px;top:1918px;width:174px;list-style:none}
.cats li{height:29px;display:flex;justify-content:space-between;align-items:center;font-size:10px;color:var(--ink);border-bottom:1px dotted var(--line)}
.cats li:last-child{border:none}
.cats em{font-style:normal;color:#c2c2c2;font-size:9px}

/* posts */
.post-img{position:absolute;width:267px;height:218px}
.post-body{position:absolute;width:235px}
.post-body h2{font-size:19px;font-weight:800;letter-spacing:.1px;white-space:nowrap}
.meta{margin-top:7px;font-size:8px;font-weight:600;letter-spacing:.8px;color:#b5b5b5}
.meta b{color:var(--teal);font-weight:600;margin-right:6px}
.meta i{font-style:normal;margin-right:6px}
.post-body p{margin-top:16px;font-size:8.8px;line-height:16.5px;color:var(--text)}
.actions{margin-top:26px;display:flex;gap:8px}
.actions span{width:33px;height:33px;border:1px solid var(--line);display:flex;align-items:center;justify-content:center}
.sep{position:absolute;left:462px;width:533px;border-top:2px dotted #e6e6e6}

/* pagination */
.page-num{position:absolute;left:462px;top:2284px;font-size:27px;font-weight:800;color:var(--teal)}
.page-total{position:absolute;left:500px;top:2288px;font-size:8px;color:var(--muted)}
.page-arrows{position:absolute;left:545px;top:2288px;display:flex;gap:8px}
.page-arrows span{width:22px;height:22px;border:1px solid var(--line);border-radius:50%;display:flex;align-items:center;justify-content:center;font-size:8px;color:#bbb}
.view-all{position:absolute;right:215px;top:2294px;font-size:9.5px;font-weight:700}

/* subscribe */
.sub-frame{position:absolute;left:569px;top:2394px;width:236px;height:219px;border:9px solid #eeeeee}
.sub-light{position:absolute;left:224px;top:2428px;width:350px;height:152px;background:var(--soft)}
.sub-light h3{position:absolute;left:62px;top:56px;font-size:31px;font-weight:800}
.sub-dark{position:absolute;left:599px;top:2428px;width:374px;height:152px;background:var(--dark)}
.sub-dark label{position:absolute;left:71px;top:70px;width:185px;height:17px;border-bottom:1px solid #555;font-size:9px;color:var(--white)}
.sub-send{position:absolute;left:267px;top:58px;width:44px;height:44px;border-radius:50%;background:var(--leaf);display:flex;align-items:center;justify-content:center}

/* cookie notice */
.cookie-notice{position:absolute;left:224px;top:2770px;width:749px;height:64px;border:1px solid var(--line);background:var(--white);display:flex;align-items:center;justify-content:space-between;padding:0 24px}
.cookie-notice p{font-size:10px;color:var(--text)}
.cookie-accept{background:var(--teal);color:var(--white);font-size:9px;font-weight:700;letter-spacing:.5px;padding:10px 20px}

/* footer */
.site-footer{position:absolute;left:0;top:2949px;width:1200px;height:200px;background:var(--dark);color:var(--white);text-align:center;padding-top:64px;font-size:13px;line-height:29.5px}
</style>
</head>
<body>

<header class="site-header">
  <div class="btn-subscribe">SUBSCRIBE</div>
  <div class="brand"><span class="brand-mark"></span><span class="brand-name">Brightmorrow</span></div>
  <div class="header-icons">
    <span class="dot-icon"></span>
    <span class="dot-icon"></span>
    <svg width="14" height="11" viewBox="0 0 14 11"><rect x="0.75" y="0.75" width="12.5" height="9.5" fill="none" stroke="#1c1d1f" stroke-width="1.3"/><path d="M1 1l6 5 6-5" fill="none" stroke="#1c1d1f" stroke-width="1.3"/></svg>
    <svg width="16" height="12" viewBox="0 0 16 12" style="margin-left:10px"><path d="M0 1h16M0 6h16M0 11h16" stroke="#1c1d1f" stroke-width="1.8"/></svg>
  </div>
</header>

<div class="hero-img hero-left" role="img" aria-label="Walker in a hat standing in a meadow at sunset"></div>
<div class="hero-img hero-main" role="img" aria-label="Close view of a person in a knitted hat among snowy grass"></div>
<div class="hero-img hero-right" role="img" aria-label="Red tulips against dark green leaves"></div>
<div class="hero-dots"><span></span><span></span></div>

<aside>
  <div class="widget-title" style="top:661px"><span>ABOUT ME</span></div>
  <div class="avatar" role="img" aria-label="Author seen from behind by a lake"></div>
  <p class="about-text">Fusce id mauris auctor, sollicitudin amet hendrerit risus. Aenean auctor erat.</p>
  <div class="about-social"><span></span><span></span><span></span><span></span></div>

  <div class="join">
    <div class="join-top">Join Us Today</div>
    <div class="join-field">Email Address
      <svg width="12" height="9" viewBox="0 0 12 9"><rect x="0.6" y="0.6" width="10.8" height="7.8" fill="none" stroke="#33b8a4" stroke-width="1.1"/><path d="M1 1l5 4 5-4" fill="none" stroke="#33b8a4" stroke-width="1.1"/></svg>
    </div>
  </div>

  <div class="widget-title" style="top:1111px"><span>RECENT POSTS</span></div>
  <div class="recent" style="top:1161px"><div class="thumb" role="img" aria-label="Cut wooden log slice" style="background:linear-gradient(135deg,#efe9e0,#b99a76)"></div><div><h4>Forest Bathing</h4><p>NOV 23.18</p></div></div>
  <div class="recent" style="top:1226px"><div class="thumb" role="img" aria-label="Moss on a stone" style="background:linear-gradient(135deg,#eef2e6,#7f9a4a)"></div><div><h4>Slow Walks</h4><p>NOV 23.18</p></div></div>
  <div class="recent" style="top:1291px"><div class="thumb" role="img" aria-label="River stones in clear water" style="background:linear-gradient(135deg,#e4eef2,#4a8fae)"></div><div><h4>Kids Outdoors</h4><p>NOV 23.18</p></div></div>

  <div class="ads"><div class="ads-inner"><b>ads</b><small>270 x 270</small></div></div>

  <div class="widget-title" style="top:1592px"><span>INSTAGRAM</span></div>
  <div class="insta">
    <div role="img" aria-label="Boat on a misty lake" style="background:linear-gradient(180deg,#e9eef0,#9bb8c4)"></div>
    <div role="img" aria-label="Backpack against a pale wall" style="background:linear-gradient(180deg,#ecebea,#3a4a3e)"></div>
    <div role="img" aria-label="Hiker in a red jacket on a trail" style="background:linear-gradient(180deg,#d9dedb,#6f8a4a)"></div>
    <div role="img" aria-label="Pale grasses in the wind" style="background:linear-gradient(135deg,#f3f1e6,#cfd4a8)"></div>
  </div>
  <div class="insta-handle">@BRIGHTMORROW</div>

  <div class="widget-title" style="top:1872px"><span>CATEGORIES</span></div>
  <ul class="cats">
    <li>Wellbeing<em>9</em></li>
    <li>Outdoors<em>7</em></li>
    <li>Walking<em>11</em></li>
    <li>Retreats<em>8</em></li>
    <li>Family<em>6</em></li>
  </ul>
</aside>

<main>
  <div class="post-img" style="left:462px;top:650px;background:linear-gradient(180deg,#e6ebe8,#8aa7a0 45%,#4f7d8c)" role="img" aria-label="Rocky coastline above the sea"></div>
  <div class="post-body" style="left:753px;top:664px">
    <h2>Calming Coastlines</h2>
    <div class="meta"><b>OUTDOORS</b><i>X</i>NOV 26.18</div>
    <p>Aenean sollicitudin, lorem quis bibendum auctor, nisi elit consequat ipsum, nec sagittis sem nibh id elit duisa. Vivamus tempus vulputate mi quis hendrerit.</p>
    <div class="actions"><span><svg width="12" height="10" viewBox="0 0 12 10"><path d="M0 5h11M7 1l4 4-4 4" fill="none" stroke="#1c1d1f" stroke-width="1.2"/></svg></span><span><svg width="11" height="11" viewBox="0 0 11 11"><path d="M5.5 1L10 9H1z" fill="none" stroke="#1c1d1f" stroke-width="1.1"/></svg></span></div>
  </div>
  <div class="sep" style="top:893px"></div>

  <div class="post-body" style="left:462px;top:934px">
    <h2>Winter Walks</h2>
    <div class="meta"><b>WALKING</b><i>X</i>NOV 25.18</div>
    <p>Aenean sollicitudin, lorem quis bibendum auctor, nisi elit consequat ipsum, nec sagittis sem nibh id elit duisa. Vivamus tempus vulputate mi quis hendrerit.</p>
    <div class="actions"><span><svg width="12" height="10" viewBox="0 0 12 10"><path d="M0 5h11M7 1l4 4-4 4" fill="none" stroke="#1c1d1f" stroke-width="1.2"/></svg></span><span><svg width="11" height="11" viewBox="0 0 11 11"><path d="M5.5 1L10 9H1z" fill="none" stroke="#1c1d1f" stroke-width="1.1"/></svg></span></div>
  </div>
  <div class="post-img" style="left:728px;top:920px;background:linear-gradient(135deg,#eef0f1,#c9b07a 55%,#6e5f38)" role="img" aria-label="Walker in a felt hat and warm coat"></div>
  <div class="sep" style="top:1163px"></div>

  <div class="post-img" style="left:462px;top:1190px;background:linear-gradient(180deg,#dcdfda,#7f8a66 40%,#c2bf9c)" role="img" aria-label="Wooden huts in a meadow below a hill"></div>
  <div class="post-body" style="left:753px;top:1204px">
    <h2>Rest in the Hills</h2>
    <div class="meta"><b>RETREATS</b><i>X</i>NOV 23.18</div>
    <p>Aenean sollicitudin, lorem quis bibendum auctor, nisi elit consequat ipsum, nec sagittis sem nibh id elit duisa. Vivamus tempus vulputate mi quis hendrerit.</p>
    <div class="actions"><span><svg width="12" height="10" viewBox="0 0 12 10"><path d="M0 5h11M7 1l4 4-4 4" fill="none" stroke="#1c1d1f" stroke-width="1.2"/></svg></span><span><svg width="11" height="11" viewBox="0 0 11 11"><path d="M5.5 1L10 9H1z" fill="none" stroke="#1c1d1f" stroke-width="1.1"/></svg></span></div>
  </div>
  <div class="sep" style="top:1433px"></div>

  <div class="post-body" style="left:462px;top:1474px">
    <h2>Sea Air for Stress</h2>
    <div class="meta"><b>WELLBEING</b><i>X</i>NOV 22.18</div>
    <p>Aenean sollicitudin, lorem quis bibendum auctor, nisi elit consequat ipsum, nec sagittis sem nibh id elit duisa. Vivamus tempus vulputate mi quis hendrerit.</p>
    <div class="actions"><span><svg width="12" height="10" viewBox="0 0 12 10"><path d="M0 5h11M7 1l4 4-4 4" fill="none" stroke="#1c1d1f" stroke-width="1.2"/></svg></span><span><svg width="11" height="11" viewBox="0 0 11 11"><path d="M5.5 1L10 9H1z" fill="none" stroke="#1c1d1f" stroke-width="1.1"/></svg></span></div>
  </div>
  <div class="post-img" style="left:728px;top:1460px;background:linear-gradient(180deg,#3c8a9c,#2d7386 55%,#7a6a52)" role="img" aria-label="Person with windswept hair by the sea"></div>
  <div class="sep" style="top:1703px"></div>

  <div class="post-img" style="left:462px;top:1730px;background:linear-gradient(160deg,#eef0e2,#c9d49a 50%,#7f9a3a)" role="img" aria-label="Picnic food on a blanket in the grass"></div>
  <div class="post-body" style="left:753px;top:1744px">
    <h2>Family Picnic Day</h2>
    <div class="meta"><b>FAMILY</b><i>X</i>NOV 19.18</div>
    <p>Aenean sollicitudin, lorem quis bibendum auctor, nisi elit consequat ipsum, nec sagittis sem nibh id elit duisa. Vivamus tempus vulputate mi quis hendrerit.</p>
    <div class="actions"><span><svg width="12" height="10" viewBox="0 0 12 10"><path d="M0 5h11M7 1l4 4-4 4" fill="none" stroke="#1c1d1f" stroke-width="1.2"/></svg></span><span><svg width="11" height="11" viewBox="0 0 11 11"><path d="M5.5 1L10 9H1z" fill="none" stroke="#1c1d1f" stroke-width="1.1"/></svg></span></div>
  </div>
  <div class="sep" style="top:1973px"></div>

  <div class="post-body" style="left:462px;top:2014px">
    <h2>Waves and Breath</h2>
    <div class="meta"><b>WELLBEING</b><i>X</i>NOV 18.18</div>
    <p>Aenean sollicitudin, lorem quis bibendum auctor, nisi elit consequat ipsum, nec sagittis sem nibh id elit duisa. Vivamus tempus vulputate mi quis hendrerit.</p>
    <div class="actions"><span><svg width="12" height="10" viewBox="0 0 12 10"><path d="M0 5h11M7 1l4 4-4 4" fill="none" stroke="#1c1d1f" stroke-width="1.2"/></svg></span><span><svg width="11" height="11" viewBox="0 0 11 11"><path d="M5.5 1L10 9H1z" fill="none" stroke="#1c1d1f" stroke-width="1.1"/></svg></span></div>
  </div>
  <div class="post-img" style="left:728px;top:2000px;background:linear-gradient(135deg,#6fb6d4,#e9f1f3 50%,#9fd0dc)" role="img" aria-label="Surfer riding through white water"></div>
  <div class="sep" style="top:2243px"></div>

  <div class="page-num">01</div>
  <div class="page-total">/ 05</div>
  <div class="page-arrows"><span>&lsaquo;</span><span>&rsaquo;</span></div>
  <div class="view-all">View All <span style="color:#bbb">&rsaquo;</span></div>
</main>

<section>
  <div class="sub-frame"></div>
  <div class="sub-light"><h3>Subscribe</h3></div>
  <div class="sub-dark">
    <label>Email Address</label>
    <div class="sub-send"><svg width="14" height="13" viewBox="0 0 14 13"><path d="M1 1l12 5.5L1 12l2-5.5z M3 6.5h10" fill="none" stroke="#1c1d1f" stroke-width="1.1" stroke-linejoin="round"/></svg></div>
  </div>
</section>

<div class="cookie-notice">
  <p>We use cookies to keep this site working well. You can change your choice at any time.</p>
  <span class="cookie-accept">ACCEPT</span>
</div>

<footer class="site-footer">
  <div>Clara Dunmore</div>
  <div>Brightmorrow</div>
  <div>Telephone +44 7946 203857</div>
  <div>brightmorrow@mailbox.example</div>
</footer>

</body>
</html>
```